Records Management Company Revamp

We are looking to revamp our web presence, and need a catchy design that helps us to get noticed! We would like the website to be in wordpress. the main requirements are a home page, a landing page template for SEO / PPC, and then a few other pages that can be reused throughout the website.

We are happy to supply content / video etc.

Number of Pages Required

3 page

Font styles to use
Other font styles liked:
• Find fonts listed in attached branding document

Requirements
Must have
• Home page as well as sub pages according to their colours. Need to use colours and fonts set out in branding guide. Attached are examples of home page and sub pages.
Nice to have
• We have uploaded some very basic ideas we have of how we wish the website to look, but looking to have it more professional and fit together. Please see uploaded items.

```html
<!DOCTYPE html>
<html lang="en">
<head>
<meta charset="utf-8">
<title>Vaultline Records — Home</title>
<link href="https://fonts.googleapis.com/css2?family=Oswald:wght@400;500;600&family=Open+Sans:wght@400;600&display=swap" rel="stylesheet">
<style>
:root{
  --ink:#1f2220;
  --black:#0d0e0e;
  --white:#ffffff;
  --blue:#1f6fb0;
  --sky:#2b92d4;
  --green:#7dbd1f;
  --orange:#f39a22;
  --red:#d9253a;
  --lime:#9ad21c;
  --grey:#6b6f73;
  --line:#d9dde0;
  --head:'Oswald',sans-serif;
  --body:'Open Sans',sans-serif;
}
*{box-sizing:border-box;margin:0;padding:0}
html,body{width:1200px;height:1200px;overflow:hidden;background:var(--white)}
.page{position:absolute;left:369px;top:0;width:580px;height:1500px;transform:scale(.8);transform-origin:0 0;font-family:var(--body);color:var(--ink);overflow:hidden}
.abs{position:absolute}
.topbar{left:0;top:0;width:580px;height:22px;background:var(--ink);color:#cfd3d6;font-size:5.5px;display:flex;align-items:center}
.topbar span{position:absolute;display:flex;align-items:center;gap:3px}
.dot{width:5px;height:5px;border-radius:50%;background:#cfd3d6;display:inline-block}
.header{top:22px;left:0;width:580px;height:46px;background:var(--white)}
.brand{font-family:var(--head);font-weight:500;color:var(--ink);display:flex;align-items:center;gap:4px}
.brand i{width:7px;height:7px;background:currentColor;display:inline-block}
.nav{left:191px;top:17px;display:flex;gap:12px;font-family:var(--head);font-size:5.5px;align-items:center}
.nav .on{background:var(--sky);color:#fff;padding:3px 9px;border-radius:2px}
.photo{background:linear-gradient(120deg,#9fb3c6,#e6ecef 45%,#c4ced6 70%,#8a98a8)}
.arrow{width:18px;height:48px;background:rgba(255,255,255,.85);display:flex;align-items:center;justify-content:center;color:#d04a4a;font-size:9px}
.form{left:360px;top:106px;width:148px;height:181px;background:#fff;border-radius:4px;box-shadow:0 2px 6px rgba(0,0,0,.2);overflow:hidden}
.form-head{background:#4aa5de;color:#fff;font-size:6px;text-align:center;height:32px;padding:9px 14px 0;line-height:1.4}
.field{position:absolute;left:10px;width:128px;height:15px;border:1px solid var(--line);font-size:5px;color:#8a8f93;padding:4px 4px}
.send{position:absolute;left:47px;top:151px;width:53px;height:15px;background:var(--sky);color:#fff;font-size:5px;text-align:center;line-height:15px}
.svc{top:367px;width:101px;height:67px;color:#fff;text-align:center}
.svc h3{font-family:var(--head);font-weight:500;font-size:8.5px;margin-top:20px}
.svc p{font-size:5px;line-height:1.5;margin-top:5px;padding:0 12px}
.svc-ico{position:absolute;left:38px;top:-14px;width:25px;height:25px;border-radius:50%;border:2px solid #fff}
.works{top:463px;left:0;width:580px;height:198px;background:#15191c}
.works h2{font-family:var(--head);font-weight:500;color:#fff;font-size:20px;position:absolute;left:72px;top:24px;letter-spacing:-.2px}
.works ul{position:absolute;left:72px;top:64px;list-style:none;color:var(--orange);font-size:5px;line-height:9.8px}
.frame{border:1px solid var(--lime);display:flex;align-items:center;justify-content:center;text-align:center;color:#fff;font-family:var(--head);font-weight:500}
.tile{top:690px;height:157px}
.feat{top:876px;width:102px}
.feat h4{height:24px;line-height:24px;color:#fff;font-family:var(--head);font-weight:500;font-size:8px;text-align:center}
.feat svg{display:block;margin:11px auto 0}
.feat p{font-size:5px;line-height:9.7px;text-align:center;margin-top:8px;color:#444}
.feat a{display:block;font-size:5px;text-align:center;text-decoration:none}
.accr{top:1010px;left:0;width:580px;text-align:center}
.accr h2{font-family:var(--head);font-weight:500;font-size:15px}
.accr p{font-size:5px;line-height:10px;color:#444;margin-top:10px}
.badge{top:1087px;width:56px;height:13px;background:#c9ced2;border-radius:2px}
.testi{left:73px;top:1131px;width:221px;height:150px;background:#1b2630;color:#fff;text-align:center}
.footer{top:1311px;left:0;width:580px;height:189px;background:var(--black);color:#9a9ea2}
.footer h5{font-family:var(--head);font-weight:500;color:#fff;font-size:7px;position:absolute}
.footer .small{font-size:5px;line-height:9.6px;position:absolute}
.social{width:10px;height:10px;border-radius:50%;border:1px solid #9a9ea2;display:inline-block;margin-right:5px}
</style>
</head>
<body>
<div class="page">

  <div class="abs topbar">
    <span style="left:73px"><span class="dot"></span>+1-202-555-0147</span>
    <span style="left:146px"><span class="dot"></span>hello@vaultline.example</span>
    <span style="left:424px;gap:5px"><span class="dot"></span><span class="dot"></span><span class="dot"></span><span class="dot"></span></span>
    <span style="left:488px">Sign in</span>
  </div>

  <header class="abs header">
    <div class="abs brand" style="left:73px;top:14px;font-size:11px"><i></i>Vaultline Records</div>
    <nav class="abs nav">
      <span class="on">HOME</span><span>OFFSITE STORAGE</span><span>DOCUMENT SHREDDING</span><span>DIGITISATION</span><span>ARCHIVE SUPPLIES</span><span>CONTACT US</span>
    </nav>
    <svg class="abs" style="left:496px;top:18px" width="12" height="11" viewBox="0 0 12 11"><path d="M0 1h2l2 6h6l1-4H3" fill="none" stroke="#1f2220" stroke-width="1.2"/><circle cx="5" cy="9.5" r="1" fill="#1f2220"/><circle cx="9" cy="9.5" r="1" fill="#1f2220"/></svg>
  </header>

  <section class="abs photo" style="left:0;top:68px;width:580px;height:256px" role="img" aria-label="Three colleagues in an office reviewing a document together"></section>
  <div class="abs arrow" style="left:40px;top:187px">&#8249;</div>
  <div class="abs arrow" style="left:523px;top:187px">&#8250;</div>
  <form class="abs form">
    <div class="form-head">Receive any of your Suggestion via Email</div>
    <div class="field" style="top:48px">Name</div>
    <div class="field" style="top:68px">Email Address</div>
    <div class="field" style="top:89px">Subject</div>
    <div class="field" style="top:109px;height:29px">Message</div>
    <div class="send">SEND MESSAGE</div>
  </form>

  <div class="abs svc" style="left:73px;background:var(--blue)"><div class="svc-ico" style="background:var(--blue)"></div><h3>OFFSITE STORAGE</h3><p>There are many variations of available, but the majority</p></div>
  <div class="abs svc" style="left:184px;background:var(--green)"><div class="svc-ico" style="background:var(--green)"></div><h3>DOCUMENT SHREDDING</h3><p>There are many variations of available, but the majority</p></div>
  <div class="abs svc" style="left:295px;background:var(--orange)"><div class="svc-ico" style="background:var(--orange)"></div><h3>DIGITISATION</h3><p>There are many variations of available, but the majority</p></div>
  <div class="abs svc" style="left:406px;background:var(--sky)"><div class="svc-ico" style="background:var(--sky)"></div><h3>ARCHIVE SUPPLIES</h3><p>There are many variations of available, but the majority</p></div>

  <section class="abs works">
    <div class="abs photo" style="left:321px;top:0;width:259px;height:198px;background:linear-gradient(90deg,#1b1f22,#3d4448 40%,#2a3034)" role="img" aria-label="Forklift moving archive boxes in a warehouse"></div>
    <h2>HOW OFFSITE STORAGE WORKS</h2>
    <ul>
      <li>We deliver boxes and labels</li>
      <li>If you need them, we get you started with all the essentials to prepare your archives</li>
      <li>We pick up your documents</li>
      <li>When your boxes are ready, let us know and we'll come by and collect your documents</li>
      <li>We Store Your Documents</li>
      <li>Your documents are stored in our secure purpose-built facility in Eastbrook</li>
      <li>We Retrieve &amp; Deliver Your Documents</li>
      <li>When you need your documents, just call or email us and we'll get them to you!</li>
      <li>We Can Securely Destroy</li>
      <li>We can work with you on determining which documents can be securely destroyed and</li>
      <li>do this for you!</li>
    </ul>
    <div class="abs frame" style="left:382px;top:66px;width:137px;height:65px;font-size:9px"><span class="brand" style="color:var(--lime)"><i></i>Vaultline Records</span></div>
  </section>

  <div class="abs tile photo" style="left:73px;width:240px;background:linear-gradient(120deg,#6f7f8c,#c9cdd0 50%,#8d99a3)" role="img" aria-label="Engineers in hard hats reviewing plans at a table"></div>
  <div class="abs frame" style="left:143px;top:752px;width:100px;height:33px;font-size:15px;background:rgba(0,0,0,.25)">OUR TEAM</div>
  <div class="abs tile photo" style="left:325px;width:183px;background:linear-gradient(120deg,#2c3236,#5f676b 50%,#34393c)" role="img" aria-label="Warehouse forklift among stacked pallets"></div>
  <div class="abs frame" style="left:339px;top:740px;width:155px;height:58px;font-size:15px;line-height:1.3">CALL TO ACTION EDITIBLE<br>TEXT ARE</div>

  <div class="abs feat" style="left:73px">
    <h4 style="background:var(--red)">SPEED</h4>
    <svg width="26" height="20" viewBox="0 0 26 20" fill="none" stroke="var(--red)" stroke-width="1.2"><rect x="2" y="3" width="13" height="11"/><path d="M15 7h5l4 4v3h-9"/><circle cx="7" cy="16" r="2"/><circle cx="20" cy="16" r="2"/></svg>
    <p>Contrary to popular belief, Lorem Ipsum is not simply random text. It roots in a piece of classical</p>
    <a style="color:var(--red)">Read More..</a>
  </div>
  <div class="abs feat" style="left:184px">
    <h4 style="background:var(--green)">ACCURACY</h4>
    <svg width="22" height="20" viewBox="0 0 22 20" fill="none" stroke="var(--green)" stroke-width="1.2"><circle cx="11" cy="10" r="8"/><circle cx="11" cy="10" r="3"/><path d="M11 0v20M1 10h20"/></svg>
    <p>Contrary to popular belief, Lorem Ipsum is not simply random text. It roots in a piece of classical</p>
    <a style="color:var(--green)">Read More..</a>
  </div>
  <div class="abs feat" style="left:295px">
    <h4 style="background:var(--orange)">PERFECTION</h4>
    <svg width="28" height="20" viewBox="0 0 28 20" fill="none" stroke="var(--orange)" stroke-width="1.2"><path d="M2 5l6 0 6 5 6-5 6 0M2 5v8h4l6 4 4-2 6-2h4V5"/></svg>
    <p>Contrary to popular belief, Lorem Ipsum is not simply random text. It roots in a piece of classical</p>
    <a style="color:var(--orange)">Read More..</a>
  </div>
  <div class="abs feat" style="left:406px">
    <h4 style="background:var(--sky)">SPEED</h4>
    <svg width="20" height="22" viewBox="0 0 20 22" fill="none" stroke="var(--sky)" stroke-width="1.2"><rect x="2" y="1" width="16" height="20"/><path d="M6 17v-4M10 17v-7M14 17v-10"/></svg>
    <p>Contrary to popular belief, Lorem Ipsum is not simply random text. It roots in a piece of classical</p>
    <a style="color:var(--sky)">Read More..</a>
  </div>

  <section class="abs accr">
    <h2>ACCREDITATION, HISTORY LOGOS ETC</h2>
    <p>There are many variations of passages of Lorem Ipsum available, but the majority have<br>suffered alteration in some form, by injected humour,</p>
  </section>
  <div class="abs badge" style="left:99px"></div>
  <div class="abs badge" style="left:180px"></div>
  <div class="abs badge" style="left:260px"></div>
  <div class="abs badge" style="left:343px"></div>
  <div class="abs badge" style="left:423px"></div>

  <section class="abs testi">
    <h3 style="font-family:var(--head);font-weight:500;font-size:11px;margin-top:14px">TESTIMONIALS</h3>
    <div class="abs" style="left:20px;top:43px;width:181px;height:64px;border:1px solid #3a4a58"></div>
    <p class="abs" style="left:20px;top:56px;width:181px;font-size:5px;line-height:9.7px;color:#cfd6dc">There are many variations of passages of Lorem Ipsum available, but the majority have suffered alteration in some form, by injected humour, or randomised words which don't</p>
    <div class="abs" style="left:76px;top:103px;width:10px;height:10px;border-radius:50%;background:#fff;color:#333;font-size:6px;line-height:10px">&#8249;</div>
    <div class="abs" style="left:99px;top:96px;width:24px;height:24px;border-radius:50%;background:#8aa3b8;border:2px solid #fff" role="img" aria-label="Client portrait"></div>
    <div class="abs" style="left:134px;top:103px;width:10px;height:10px;border-radius:50%;background:#fff;color:#333;font-size:6px;line-height:10px">&#8250;</div>
    <p class="abs" style="left:0;top:128px;width:221px;font-size:6px;font-style:italic">Mara Ellison</p>
  </section>

  <div class="abs photo" style="left:306px;top:1131px;width:201px;height:150px;background:linear-gradient(120deg,#55636d,#aab3b9 50%,#6d7880)" role="img" aria-label="Workers in hard hats studying site plans"></div>
  <div class="abs frame" style="left:343px;top:1191px;width:127px;height:30px;font-size:14px;background:rgba(0,0,0,.2)">AREAS WE SERVICE</div>

  <footer class="abs footer">
    <div class="abs brand" style="left:88px;top:32px;font-size:10px;color:#fff"><i></i>Vaultline Records</div>
    <p class="small" style="left:88px;top:60px;width:125px">There are many variations of passages of Lorem Ipsum available, but the majority have suffered alteration in some form, by injected humour, or randomised words which don't look even slightly believable. If you are going to use</p>
    <div class="abs" style="left:88px;top:121px"><span class="social"></span><span class="social"></span><span class="social"></span><span class="social"></span></div>
    <h5 style="left:255px;top:36px">RECENT POSTS</h5>
    <p class="small" style="left:255px;top:60px">10 established fact that<br>2019 a reader</p>
    <p class="small" style="left:255px;top:84px">Established fact that<br>2019 a reader</p>
    <p class="small" style="left:255px;top:107px">100 established fact that<br>2019 a reader</p>
    <p class="small" style="left:255px;top:131px">10 established fact that<br>2019 a reader</p>
    <h5 style="left:362px;top:36px">QUICK CONTACT</h5>
    <p class="small" style="left:362px;top:60px;font-size:6.5px;color:#cfd3d6"><span style="color:var(--sky)">&#9679;</span> +1-202-555-0147</p>
    <p class="small" style="left:362px;top:75px;font-size:6px;color:#cfd3d6"><span style="color:var(--sky)">&#9679;</span> hello@vaultline.example</p>
    <h5 style="left:362px;top:97px">SUBSCRIBE NEWSLETTER</h5>
    <div class="abs" style="left:362px;top:117px;width:99px;height:17px;background:#fff;font-size:5px;color:#999;padding:5px 4px">Your Email</div>
    <div class="abs" style="left:461px;top:117px;width:31px;height:17px;background:var(--sky)">
      <svg width="31" height="17" viewBox="0 0 31 17"><path d="M11 9l10-5-3 9-2-3z" fill="#fff"/></svg>
    </div>
    <div class="abs" style="left:0;top:171px;width:580px;height:18px;border-top:1px solid #222;font-size:5px;text-align:center;line-height:18px">@Vaultline Records 2019</div>
  </footer>

</div>
</body>
</html>
```